Harborline Energy - needs a business card

Harborline Energy is a U.S. based diesel sourcing and distribution company that supports American oil & gas fields through providing quality product and consistent services.

Target Market(s)

Oil and Gas

Contact Information for Business Card

The background of the card must be white to ensure the logo pops.

Font styles to use
Serif
Sans Serif

Colors

Designer to choose colors to be used in the design.

Requirements
Must have
• Front of Card: Tag line: Harborline Energy, Powering America's Oil & Gas fields.
• Not sure if you guys do this part but just in case...
• Dale Menschow
• Owner/CEO
• C:555.318.4076
• E:Dmenschow@harborlineenergy.example
• W:Harborlineenergy.example
• Locations: Servicing the Powder River, DJ basin and Bakken formations.
• Back of Card: " Frac fueling is what we do. We understand how important diesel fuel is to your operation, which is why our main service line is Frac fueling. We assure our supply and stand by our service"

```html
<!DOCTYPE html>
<html lang="en">
<head>
<meta charset="utf-8">
<title>Harborline Energy – Business Card</title>
<link rel="stylesheet" href="https://fonts.googleapis.com/css2?family=Lato:wght@400;700&display=swap">
<style>
  :root {
    --backdrop: #1c1c1e;
    --card: #ffffff;
    --card-edge: #d9d9db;
    --pattern-light: #f4f4f5;
    --pattern-dark: #dcdcde;
    --text: #1f1f21;
    --red: #c8202b;
    --blue: #27418f;
  }
  * { margin: 0; padding: 0; box-sizing: border-box; }
  html, body { width: 1200px; height: 900px; overflow: hidden; background: var(--backdrop); }
  body { font-family: "Lato", sans-serif; color: var(--text); position: relative; }

  .card {
    position: absolute;
    left: 250px;
    width: 700px;
    height: 400px;
    background: var(--card);
    border: 1px solid var(--card-edge);
    overflow: hidden;
  }
  .card--back { top: 30px; }
  .card--front { top: 470px; }

  /* back */
  .back__pattern {
    position: absolute; inset: 0;
    background: linear-gradient(120deg, var(--pattern-light) 0%, var(--pattern-dark) 100%);
  }
  .back__statement {
    position: absolute;
    left: 0; right: 0; top: 205px;
    text-align: center;
    font-size: 18px;
    line-height: 1.3;
    color: var(--text);
  }

  /* front */
  .brand {
    position: absolute;
    left: 40px; top: 120px;
    width: 230px;
    display: flex; flex-direction: column; align-items: center; gap: 14px;
  }
  .brand__dot { width: 70px; height: 70px; border-radius: 50%; background: var(--blue); }
  .brand__name {
    font-size: 26px; font-weight: 700; color: var(--blue);
    text-transform: uppercase; letter-spacing: 1px; text-align: center; line-height: 1.1;
  }
  .divider {
    position: absolute; left: 298px; top: 70px;
    width: 2px; height: 210px; background: var(--red);
  }
  .contact { position: absolute; left: 326px; top: 74px; }
  .contact__name {
    font-size: 30px; font-weight: 700; color: var(--red);
    text-transform: uppercase; letter-spacing: 1px; line-height: 1;
  }
  .contact__title { font-size: 17px; margin-top: 4px; }
  .contact__region { font-size: 17px; line-height: 1.3; margin-top: 16px; }
  .contact__list { list-style: none; margin-top: 12px; }
  .contact__item { display: flex; align-items: center; gap: 9px; font-size: 16px; line-height: 1.5; }
  .contact__icon { width: 12px; height: 12px; flex: none; }
  .tagline {
    position: absolute; left: 0; right: 0; bottom: 40px;
    text-align: center; font-size: 21px;
  }
</style>
</head>
<body>
  <section class="card card--back">
    <div class="back__pattern" role="img" aria-label="Embossed repeating pattern of the brand symbol"></div>
    <p class="back__statement">
      Frac fueling is what we do.<br>
      We understand how important diesel fuel is to your operation,<br>
      which is why our main service line is Frac fueling.<br>
      We assure our supply and stand by our service"
    </p>
  </section>

  <section class="card card--front">
    <div class="brand">
      <span class="brand__dot"></span>
      <span class="brand__name">Harborline Energy</span>
    </div>
    <span class="divider"></span>
    <div class="contact">
      <h1 class="contact__name">Dale Menschow</h1>
      <p class="contact__title">Owner/CEO</p>
      <p class="contact__region">Servicing the Powder River,<br>DJ basin and Bakken formations.</p>
      <ul class="contact__list">
        <li class="contact__item">
          <svg class="contact__icon" viewBox="0 0 16 16"><path d="M3 1l3 0 1 4-2 1c1 2 3 4 5 5l1-2 4 1 0 3c0 1-1 2-2 2C7 15 1 9 1 3c0-1 1-2 2-2z" fill="var(--red)"/></svg>
          555.318.4076
        </li>
        <li class="contact__item">
          <svg class="contact__icon" viewBox="0 0 16 16"><rect x="1" y="3" width="14" height="10" fill="none" stroke="var(--red)" stroke-width="1.6"/><path d="M1 3l7 6 7-6" fill="none" stroke="var(--red)" stroke-width="1.6"/></svg>
          Dmenschow@harborlineenergy.example
        </li>
        <li class="contact__item">
          <svg class="contact__icon" viewBox="0 0 16 16"><circle cx="8" cy="8" r="6.5" fill="none" stroke="var(--red)" stroke-width="1.4"/><path d="M1.5 8h13M8 1.5c-3 3.5-3 9.5 0 13M8 1.5c3 3.5 3 9.5 0 13" fill="none" stroke="var(--red)" stroke-width="1.2"/></svg>
          www.harborlineenergy.example
        </li>
      </ul>
    </div>
    <p class="tagline">Harborline Energy, Powering America's Oil &amp; Gas fields.</p>
  </section>
</body>
</html>
```